Promo Flyer to put in prize bags at carnival

I am owner of Willow & Pike Hair Salon located in Gahanna, OH. I’m sponsoring a community carnival when I will be putting flyers in all attendees prize bags. This flyer will communicate details of my salon on one side (picture of me, logo, description of business, address, website, email, phone #) and the other side will showcase and a 50% discount for first time customers. Flyer can be 5” x 7” or greater

Side 1 details:
-Logo will be attached to this brief
-picture of me will be attached to this brief
-address: 2641 W. Brockton Ave, Suite 17, Gahanna, OH, 43230
-website: wphairstudio.example
-email: Dorian.blake@wphairstudio.example
-phone: 614-55-GOWPS (46977)

Side 2 details:
-‘Guess what? You get 50% off your 1st service at Willow & Pike Hair Salon.’
-‘Expires 7/31/2018’
-Hair | Fashion | Photography
-Visit wphairstudio.example to book your service
-must present this flyer at time of service to receive discount

Industry/Entity Type

Hair And Beauty

Font styles to use
Other font styles liked:
• Inoxida

Colors
3176b5
000000
ffffff

Requirements
Must have
• 2 sides
• Color scheme to match logo

```html
<!DOCTYPE html>
<html lang="en">
<head>
<meta charset="utf-8">
<title>Willow &amp; Pike Hair Salon – Carnival Flyer</title>
<link rel="stylesheet" href="https://fonts.googleapis.com/css2?family=Lato:wght@400;700;900&family=Great+Vibes&family=Cormorant+Garamond:ital,wght@1,500&display=swap">
<style>
  :root {
    --page: #d7d8da;
    --ink: #1c1c1c;
    --dark: #242424;
    --blue: #4cc0ec;
    --blue-deep: #2a9fd0;
    --orange: #f0a624;
    --white: #ffffff;
    --navy: #14213a;
  }
  * { box-sizing: border-box; margin: 0; padding: 0; }
  html, body { width: 1200px; height: 857px; overflow: hidden; }
  body { background: var(--page); font-family: "Lato", sans-serif; position: relative; }

  .flyer { position: absolute; top: 50px; width: 540px; height: 756px; overflow: hidden; box-shadow: 0 6px 18px rgba(0,0,0,.25); }
  .flyer--info { left: 40px; background: var(--dark); }
  .flyer--offer { left: 620px; background: var(--ink); }

  /* Info side */
  .backdrop { position: absolute; inset: 0; background: linear-gradient(160deg, #3d3d3d 0%, #2a2a2a 45%, #1d1d1d 100%); }
  .logo-badge { position: absolute; left: 160px; top: -95px; width: 230px; height: 230px; border-radius: 50%; background: var(--white); border: 7px solid var(--blue); display: flex; align-items: flex-end; justify-content: center; padding-bottom: 44px; }
  .logo-name { font-family: "Lato", sans-serif; font-weight: 700; font-size: 23px; color: var(--ink); }
  .about { position: absolute; left: 40px; top: 170px; width: 460px; text-align: center; font-family: "Cormorant Garamond", serif; font-style: italic; font-weight: 500; font-size: 23px; line-height: 1.3; color: var(--white); }
  .about-sign { display: block; margin-top: 6px; color: var(--blue); font-size: 26px; }
  .contact-band { position: absolute; left: 0; bottom: 0; width: 540px; height: 190px; }
  .portrait-ring { position: absolute; left: 240px; top: 385px; width: 300px; height: 300px; border-radius: 50%; background: var(--orange); }
  .portrait { position: absolute; left: 256px; top: 401px; width: 268px; height: 268px; border-radius: 50%; background: radial-gradient(circle at 50% 55%, #1f4f63 0%, #2f6f86 38%, var(--blue) 72%); }
  .contact { position: absolute; left: 26px; bottom: 66px; color: var(--ink); line-height: 1.25; }
  .contact-phone { font-weight: 900; font-size: 21px; }
  .contact-line { font-size: 16px; }
  .site { position: absolute; left: 26px; bottom: 14px; font-weight: 900; font-size: 24px; color: var(--navy); }

  /* Offer side */
  .headline { position: absolute; left: 0; right: 0; top: 22px; text-align: center; font-family: "Great Vibes", cursive; font-size: 68px; color: var(--blue); line-height: 1; }
  .subline { position: absolute; left: 60px; right: 60px; top: 104px; text-align: center; color: var(--white); font-size: 20px; line-height: 1.3; }
  .subline strong { color: var(--orange); font-weight: 900; font-size: 26px; }
  .photo-strip { position: absolute; left: 0; top: 160px; width: 540px; height: 270px; }
  .snap { position: absolute; left: 36px; width: 220px; border-radius: 14px; border: 4px solid var(--blue); }
  .snap--cuts { top: 450px; height: 150px; background: linear-gradient(135deg, #5a4a3e, #c9bcb0 55%, #3a3a3a); }
  .snap--team { top: 618px; height: 118px; background: linear-gradient(135deg, #2d3f66, #d8d8d8 50%, #1d2c52); }
  .services { position: absolute; right: 34px; top: 440px; text-align: right; color: var(--white); font-weight: 900; font-size: 33px; line-height: 1.12; letter-spacing: .5px; }
  .services span { display: block; }
  .services .dash::after { content: ""; display: inline-block; width: 30px; height: 9px; margin-left: 10px; border-radius: 5px; background: var(--blue); vertical-align: middle; }
  .expires { position: absolute; right: 22px; top: 578px; width: 250px; padding: 8px 0; border-radius: 26px; background: var(--orange); text-align: center; color: var(--ink); font-weight: 900; font-size: 26px; }
  .visit { position: absolute; right: 30px; top: 636px; text-align: right; color: var(--white); font-size: 15px; line-height: 1.2; }
  .visit b { color: var(--blue); font-weight: 900; font-size: 21px; }
  .notice { position: absolute; right: 0; top: 690px; width: 270px; padding: 8px 18px 8px 24px; border-radius: 24px 0 0 24px; background: var(--blue); color: var(--ink); font-weight: 700; font-size: 13px; line-height: 1.25; text-align: right; }
</style>
</head>
<body>

<section class="flyer flyer--info" aria-label="Flyer side one: salon details">
  <div class="backdrop" role="img" aria-label="Faint, darkened photo of the salon interior"></div>
  <div class="logo-badge"><span class="logo-name">Willow &amp; Pike</span></div>
  <p class="about">Membership salon offering unlimited hair services and exclusive image consulting tailored to who you are and where you're going. Join a community where being set apart is a way of life…
    <span class="about-sign">Willow &amp; Pike.</span></p>
  <svg class="contact-band" viewBox="0 0 540 190" aria-hidden="true">
    <path d="M0 30 L220 30 C260 30 280 0 320 0 L540 0 L540 190 L0 190 Z" fill="var(--orange)"/>
    <path d="M0 135 L320 135 C380 135 420 100 450 80 L540 80 L540 190 L0 190 Z" fill="var(--blue)"/>
  </svg>
  <div class="portrait-ring"></div>
  <div class="portrait" role="img" aria-label="Photo of the salon owner in a teal suit and sunglasses"></div>
  <div class="contact">
    <p class="contact-phone">614-55-GOWPS (46977)</p>
    <p class="contact-line">2641 W. Brockton Ave, Suite 17,<br>Gahanna, OH, 43230</p>
    <p class="contact-line">Dorian.blake@wphairstudio.example</p>
  </div>
  <p class="site">www.wphairstudio.example</p>
</section>

<section class="flyer flyer--offer" aria-label="Flyer side two: first visit discount">
  <h1 class="headline">Guess what?</h1>
  <p class="subline">You get <strong>50%</strong> off your 1st service at Willow &amp; Pike Hair Salon</p>
  <svg class="photo-strip" viewBox="0 0 540 270" role="img" aria-label="Three side-profile photos of a client's fresh haircut">
    <defs>
      <linearGradient id="stripTone" x1="0" y1="0" x2="1" y2="0">
        <stop offset="0" stop-color="#3b2e28"/>
        <stop offset=".5" stop-color="#8c6d5c"/>
        <stop offset="1" stop-color="#d9d4cf"/>
      </linearGradient>
    </defs>
    <path d="M0 90 C150 20 390 10 540 0 L540 160 C390 200 150 250 0 270 Z" fill="url(#stripTone)"/>
    <path d="M0 90 C150 20 390 10 540 0" fill="none" stroke="var(--blue)" stroke-width="7"/>
    <path d="M0 270 C150 250 390 200 540 160" fill="none" stroke="var(--blue)" stroke-width="7"/>
    <line x1="180" y1="40" x2="200" y2="250" stroke="var(--white)" stroke-width="3"/>
    <line x1="360" y1="15" x2="380" y2="205" stroke="var(--white)" stroke-width="3"/>
  </svg>
  <div class="snap snap--cuts" role="img" aria-label="Collage of a client's haircut from four angles"></div>
  <div class="snap snap--team" role="img" aria-label="Collage of stylists fitting suits on clients"></div>
  <p class="services"><span class="dash">HAIR</span><span class="dash">FASHION</span><span>PHOTOGRAPHY</span></p>
  <p class="expires">Expires 7/31/2018</p>
  <p class="visit">Visit <b>wphairstudio.example</b><br>to book your service</p>
  <p class="notice">must present this flyer<br>at time of service to receive discount</p>
</section>

</body>
</html>
```